Plumwave business card

We need a modern business card - With our 4 colors - See web: www.plumwave.dk

I have attached logo and som old business Cards we have - Lets Make the new ones shine...:-) -

Industry/Entity Type

Business

Requirements
Must have
• the logo with plumwave only,

```html
<!DOCTYPE html>
<html lang="da">
<head>
<meta charset="utf-8">
<title>Plumwave – visitkort</title>
<link rel="stylesheet" href="https://fonts.googleapis.com/css2?family=Quicksand:wght@400;600;700&display=swap">
<style>
  :root {
    --bg: #e7e7e7;
    --paper: #ffffff;
    --orange: #e27a1e;
    --green: #7dc243;
    --magenta: #c2176f;
    --purple: #5b1a5c;
    --ink: #555555;
  }
  * { margin: 0; padding: 0; box-sizing: border-box; }
  html, body { width: 1200px; height: 665px; overflow: hidden; }
  body {
    background: var(--bg);
    font-family: "Quicksand", sans-serif;
    display: flex;
    align-items: center;
    justify-content: center;
    gap: 80px;
  }
  .card {
    position: relative;
    width: 460px;
    height: 270px;
    background: var(--paper);
    overflow: hidden;
    box-shadow: 0 18px 40px rgba(0,0,0,0.18);
  }
  .card-front .colour-field {
    position: absolute;
    left: 0;
    bottom: 0;
    width: 290px;
    height: 225px;
    border-top-right-radius: 100% 100%;
    background: radial-gradient(circle at 0% 100%,
      var(--purple) 0%, var(--magenta) 45%, var(--green) 72%, var(--orange) 100%);
  }
  .card-back .colour-field {
    position: absolute;
    inset: 0;
    background: radial-gradient(circle at 50% 50%,
      var(--purple) 20%, var(--magenta) 45%, var(--green) 70%, var(--orange) 100%);
  }
  .card-front .details {
    position: absolute;
    top: 34px;
    left: 220px;
    width: 220px;
  }
  .brand {
    display: flex;
    align-items: center;
    gap: 8px;
    color: var(--green);
    font-weight: 600;
    font-size: 17px;
    letter-spacing: 1px;
    margin-bottom: 14px;
  }
  .brand-dot {
    width: 14px; height: 14px;
    border-radius: 50%;
    background: var(--green);
    flex: none;
  }
  .person-name {
    color: var(--purple);
    font-weight: 700;
    font-size: 22px;
    line-height: 1.1;
    white-space: nowrap;
  }
  .person-title {
    color: var(--purple);
    font-weight: 600;
    font-size: 12px;
    margin-top: 3px;
  }
  .contact { list-style: none; margin-top: 34px; }
  .contact li {
    display: flex;
    align-items: center;
    gap: 8px;
    color: var(--ink);
    font-size: 14px;
    font-weight: 600;
    margin-bottom: 6px;
  }
  .contact-icon { width: 16px; height: 16px; flex: none; display: block; }
  .card-back .emblem {
    position: absolute;
    left: 50%; top: 50%;
    transform: translate(-50%, -50%);
    width: 136px;
    height: 136px;
    border-radius: 50%;
    background: var(--paper);
    display: flex;
    flex-direction: column;
    justify-content: center;
    align-items: stretch;
    padding: 0 12px;
    text-align: center;
  }
  .card-back .brand { justify-content: center; margin-bottom: 0; font-size: 16px; }
  .tagline-rule { height: 1px; background: var(--green); margin: 5px 4px 4px; }
  .tagline { font-size: 8px; color: var(--ink); font-weight: 600; }
</style>
</head>
<body>

  <article class="card card-front">
    <div class="colour-field" role="img" aria-label="Dekorativt farvefelt i orange, grøn, magenta og lilla"></div>
    <div class="details">
      <div class="brand"><span class="brand-dot"></span>plumwave</div>
      <h1 class="person-name">Maren Holmgaard</h1>
      <p class="person-title">Salgsdirektør</p>
      <ul class="contact">
        <li>
          <svg class="contact-icon" viewBox="0 0 16 16" aria-hidden="true"><circle cx="8" cy="8" r="7" fill="none" stroke="var(--ink)"/><path d="M5.5 4.5l1.5 1.5-1 1a5 5 0 0 0 3 3l1-1 1.5 1.5-1 1c-3 0-6-3-6-6z" fill="var(--ink)"/></svg>
          +45 40 12 34 56
        </li>
        <li>
          <svg class="contact-icon" viewBox="0 0 16 16" aria-hidden="true"><circle cx="8" cy="8" r="7" fill="none" stroke="var(--ink)"/><rect x="4.5" y="5.5" width="7" height="5" fill="none" stroke="var(--ink)"/><path d="M4.5 5.5l3.5 3 3.5-3" fill="none" stroke="var(--ink)"/></svg>
          mh@plumwave.dk
        </li>
      </ul>
    </div>
  </article>

  <article class="card card-back">
    <div class="colour-field" role="img" aria-label="Dekorativt farvefelt i orange, grøn, magenta og lilla"></div>
    <div class="emblem">
      <div class="brand"><span class="brand-dot"></span>plumwave</div>
      <div class="tagline-rule"></div>
      <p class="tagline">lyd til alle</p>
    </div>
  </article>

</body>
</html>
```